Financial Sevices firm looking for Brochure design

Our company Veltmoor Capital and Holdings Limited (VeltHoldings)
i
Is an investment/advisory firm - www.veltholdings-grp.net
We invest in the energy sector in Africa and offer advisory services to Energy companies looking to invest in Africa. From oil and gas, to renewables (wind/solar). We are more focused on the "West African" Sub region
We need corporate brochure (Booklet style) to circulate to our corporate clients
We would like to see a design that considers the colours in our Logo (see website)
HI Guys, sorry been travelling. Seen some very good submissions and will be sending updates shortly
Reason: Dear Designers,
Thank you for participating in this project and for some of the great designs i've received so far. Unfortunately, due to the holidays, it has been difficult to consult with other members of my team. As a result, the project deadline is extended by about 12 days
I appreciate your understanding in the situation and looking forward to continuing the excellent collaboration in the coming days
Reason: Hi All,
Apologies for the multiple deadline extensions and thanks so much for all the designs which my team and I will be reviewing today and tomorrow.
We will be closing this project tomorrow by 6pm GMT (17th Jan 2014)
Thanks to all those that submitted such wonderful designs and goodluck!!
Project to be closed finally on 17th Jan 2014 at 6pm GMT
Banks, Investment Firms, Energy companies, Private Equity Funds
I have attached a Brochure that I created myself as an example of the type of information required but please also feel free to visit our website www.veltholdings-grp.net
Looking for any creative ideas you have to suplement the information provided.
Financial

```html
<!DOCTYPE html>
<html lang="en">
<head>
<meta charset="utf-8">
<title>VeltHoldings — Corporate Profile Cover</title>
<link href="https://fonts.googleapis.com/css2?family=Libre+Baskerville:wght@400&display=swap" rel="stylesheet">
<style>
  :root {
    --backdrop: #d9dadc;
    --page: #ffffff;
    --text-grey: #4a4a4a;
    --gold-deep: #8a5a12;
    --gold-light: #e2a63a;
    --sky-deep: #2f7fbf;
    --sky-light: #b9daf0;
    --portrait-warm: #9a6f66;
    --portrait-cool: #c9c9c4;
  }
  * { margin: 0; padding: 0; box-sizing: border-box; }
  html, body {
    width: 1200px;
    height: 960px;
    overflow: hidden;
    background: var(--backdrop);
  }
  .canvas {
    position: relative;
    width: 1200px;
    height: 960px;
  }
  .booklet-cover {
    position: absolute;
    left: 220px;
    top: 100px;
    width: 760px;
    height: 760px;
    background: var(--page);
    overflow: hidden;
    box-shadow: 0 18px 40px rgba(0, 0, 0, 0.18);
  }
  .photo-cluster {
    position: absolute;
    inset: 0;
  }
  .title-block {
    position: absolute;
    left: 330px;
    top: 398px;
    display: flex;
    flex-direction: column;
    align-items: flex-end;
    gap: 34px;
  }
  .brand-name {
    font-family: "Libre Baskerville", serif;
    font-weight: 400;
    font-size: 50px;
    line-height: 1;
    color: var(--text-grey);
  }
  .document-title {
    font-family: "Libre Baskerville", serif;
    font-weight: 400;
    font-size: 22px;
    line-height: 1;
    color: var(--text-grey);
  }
</style>
</head>
<body>
<main class="canvas">
  <section class="booklet-cover">
    <svg class="photo-cluster" width="760" height="760" viewBox="0 0 760 760">
      <defs>
        <linearGradient id="industry-tones" x1="0" y1="0" x2="1" y2="1">
          <stop offset="0" stop-color="#2f7fbf"/>
          <stop offset="0.3" stop-color="#e2a63a"/>
          <stop offset="1" stop-color="#8a5a12"/>
        </linearGradient>
        <linearGradient id="community-tones" x1="0" y1="0" x2="1" y2="0">
          <stop offset="0" stop-color="#c9c9c4"/>
          <stop offset="1" stop-color="#9a6f66"/>
        </linearGradient>
        <linearGradient id="wind-tones" x1="0" y1="0" x2="0" y2="1">
          <stop offset="0" stop-color="#2f7fbf"/>
          <stop offset="1" stop-color="#b9daf0"/>
        </linearGradient>
      </defs>

      <g class="photo-tile photo-tile--industry" role="img" aria-label="Photo of a golden lit industrial energy structure against a blue sky">
        <rect x="-90" y="-90" width="180" height="180" rx="22"
              fill="url(#industry-tones)"
              transform="translate(330 20) scale(1.45 1) rotate(45)"/>
      </g>

      <g class="photo-tile photo-tile--community" role="img" aria-label="Photo of a young person in a pink top, looking aside">
        <rect x="-75" y="-75" width="150" height="150" rx="20"
              fill="url(#community-tones)"
              transform="translate(40 170) scale(1.4 1) rotate(45)"/>
      </g>

      <g class="photo-tile photo-tile--wind" role="img" aria-label="Photo of a wind turbine against a bright blue sky">
        <rect x="-85" y="-85" width="170" height="170" rx="22"
              fill="url(#wind-tones)"
              transform="translate(230 320) scale(1.45 1) rotate(45)"/>
      </g>
    </svg>

    <div class="title-block">
      <span class="brand-name">VeltHoldings</span>
      <p class="document-title">Corporate Profile</p>
    </div>
  </section>
</main>
</body>
</html>
```